massage therapy Business Card Design

massage therapy business card
I would like a custom logo created as well.
My vision is angel wings with the HB business initials in between them.
A very simple design.
Colors preferred are light blues and greens.

Target Market(s)

Massage, Spa, fitness

Industry/Entity Type

Massage Therapy

Contact Information for Business Card

A Harbor Breeze
Nora Campe
Massage Therapist and Veldane Pulse Method Practitioner
2870 Marlow Ridge Road, Elmsworth, KS 66712
501-384-6190
nora.harborbreeze@mailvinto.com

Colors
abd036
33a6d7
3176b5
0255a3
0392cd
9bcb3c
cadf82

Requirements
Must have
• the logo must have angel wing.

```html
<!DOCTYPE html>
<html lang="en">
<head>
<meta charset="utf-8">
<title>A Harbor Breeze – Business Card</title>
<link rel="stylesheet" href="https://fonts.googleapis.com/css2?family=Michroma&family=Exo+2:wght@700&family=Arimo:ital,wght@1,700&display=swap">
<style>
  :root {
    --card-white: #ffffff;
    --lime: #9bff00;
    --royal-blue: #0a2fd8;
    --sky-blue: #33a6d7;
  }
  html, body {
    margin: 0;
    padding: 0;
    overflow: hidden;
    background: var(--card-white);
  }
  .card {
    position: relative;
    width: 1200px;
    height: 702px;
    overflow: hidden;
    background: var(--card-white);
  }
  .card-curves {
    position: absolute;
    inset: 0;
  }
  .brand-mark {
    position: absolute;
    left: 150px;
    top: 105px;
    display: flex;
    align-items: center;
    gap: 26px;
  }
  .brand-mark__dot {
    width: 54px;
    height: 54px;
    border-radius: 50%;
    background: var(--sky-blue);
  }
  .brand-mark__name {
    font-family: "Michroma", sans-serif;
    font-size: 120px;
    color: var(--royal-blue);
    line-height: 1;
  }
  .identity {
    position: absolute;
    left: 440px;
    top: 270px;
    width: 640px;
    text-align: center;
    font-family: "Michroma", sans-serif;
    font-size: 32px;
    line-height: 62px;
    color: var(--lime);
    -webkit-text-stroke: 2.4px var(--royal-blue);
    paint-order: stroke fill;
    text-shadow: 3px 4px 4px rgba(0, 0, 0, 0.35);
    letter-spacing: 2px;
    text-transform: uppercase;
  }
  .identity p { margin: 0; }
  .role {
    position: absolute;
    left: 121px;
    top: 413px;
    margin: 0;
    font-family: "Arimo", sans-serif;
    font-style: italic;
    font-weight: 700;
    font-size: 22px;
    color: var(--royal-blue);
    text-transform: uppercase;
    letter-spacing: 2.3px;
    white-space: nowrap;
  }
  .contact {
    position: absolute;
    right: 62px;
    top: 528px;
    margin: 0;
    text-align: right;
    font-family: "Exo 2", sans-serif;
    font-weight: 700;
    font-size: 33px;
    line-height: 47px;
    color: var(--royal-blue);
    font-style: normal;
    white-space: nowrap;
  }
  .contact span { display: block; }
  .contact__email { font-size: 31px; }
</style>
</head>
<body>
<main class="card">
  <svg class="card-curves" width="1200" height="702" viewBox="0 0 1200 702" aria-hidden="true">
    <path d="M630 20 L1152 20 L1152 328 C1060 190 900 70 630 20 Z" fill="var(--lime)"/>
    <path d="M25 382 C140 520 320 640 540 691 L25 691 Z" fill="var(--lime)"/>
  </svg>

  <div class="brand-mark">
    <span class="brand-mark__dot"></span>
    <span class="brand-mark__name">HB</span>
  </div>

  <header class="identity">
    <p class="identity__business">A Harbor Breeze</p>
    <p class="identity__person">Nora Campe</p>
  </header>

  <p class="role">Massage Therapist and Veldane Pulse Method Practitioner</p>

  <address class="contact">
    <span class="contact__address">2870 Marlow Ridge Road, Elmsworth, KS 66712</span>
    <span class="contact__phone">501-384-6190</span>
    <span class="contact__email">nora.harborbreeze@mailvinto.com</span>
  </address>
</main>
</body>
</html>
```